Shopify Theme design for a Subscription Cyber security service for consumers and SMB

Looking for the Theme design for our shopify store that will be selling a Cyber Security subscription service to Consumers and SMB. The service provides enterprise grade tools at consumer prices.
we have logos and colour scheme ready to go, however we don't use 2, 4, 7 or 8 typically in what we do.
it will be a pretty simple shop and it will be using the subscriptions app from shopify also.
We will need all the standard pages such as:
the home page
pages
Product/Subscription page
Cart
404
And any others that are standard in a theme that I have not listed
Cyber Security
Coded - Design and coding required
4 page

```html
<!DOCTYPE html>
<html lang="en">
<head>
<meta charset="utf-8">
<title>Veltrashield – Cyber Security Subscriptions</title>
<link rel="stylesheet" href="https://fonts.googleapis.com/css2?family=Lexend:wght@400;500;600&family=Lato:wght@400;700&display=swap">
<style>
:root{
  --navy:#0f1a2e;
  --ink:#1c2233;
  --text:#4a4f5c;
  --sky:#3fb0ec;
  --sky-dark:#1e8fd0;
  --purple:#5a1fd6;
  --purple-deep:#4316b8;
  --pale:#eef6f8;
  --cream:#f7f3f2;
  --line:#e3e7ee;
  --white:#ffffff;
  --black:#000000;
}
*{box-sizing:border-box;margin:0;padding:0}
html,body{width:1200px;height:4289px;overflow:hidden}
body{font-family:"Lato",sans-serif;color:var(--text);background:var(--white);position:relative}
h1,h2,h3,h4,.brand,.nav,.btn{font-family:"Lexend",sans-serif}
section,header,footer{position:relative;width:1200px;overflow:hidden}
.abs{position:absolute}

/* header */
.site-header{height:83px;background:var(--white)}
.brand{left:98px;top:25px;display:flex;align-items:center;gap:10px;font-size:23px;font-weight:500;letter-spacing:1.5px;color:var(--ink)}
.brand-mark{width:30px;height:30px;background:var(--sky);border-radius:4px}
.nav{left:489px;top:31px;display:flex;gap:27px;font-size:16px;color:var(--ink)}
.nav .active{color:var(--sky);text-decoration:underline}
.nav-icons{left:870px;top:30px;display:flex;gap:22px}
.cart-badge{position:absolute;right:-10px;top:-8px;width:14px;height:14px;border-radius:50%;background:var(--ink);color:#fff;font-size:9px;text-align:center;line-height:14px}
.btn{display:inline-block;border:none;font-weight:500;text-align:center}
.btn-sky{background:var(--sky);color:#fff;border-radius:3px}
.header-cta{left:969px;top:18px;width:133px;height:47px;line-height:47px;font-size:16px}

/* hero */
.hero{height:599px;background:var(--navy)}
.hero-art{right:0;top:0;width:640px;height:599px;background:radial-gradient(circle at 400px 250px,#24c6ff 0,#0f6da8 14%,#0c2c4f 38%,var(--navy) 70%)}
.hero h1{left:98px;top:118px;font-size:55px;line-height:78px;font-weight:500;color:#fff;letter-spacing:1px}
.hero p{left:98px;top:268px;width:430px;font-size:15px;line-height:32px;color:#e6ecf4}
.hero .btn{left:98px;top:390px;width:152px;height:48px;line-height:48px;font-size:15px}

/* shared headings */
.section-title{position:absolute;left:0;width:1200px;text-align:center;font-size:31px;font-weight:500;color:var(--ink);line-height:42px}
.title-bar{position:absolute;left:575px;width:50px;height:3px;background:var(--ink)}
.lead{position:absolute;left:145px;width:910px;text-align:center;font-size:15px;line-height:31px;color:var(--text)}

/* what we do */
.what{height:840px;background:var(--pale)}
.feature{left:98px;width:240px;height:76px;background:#fff;border:1px solid var(--line);display:flex;align-items:center;gap:14px;padding:0 12px;font-size:13px;line-height:22px;color:var(--ink)}
.feature svg{flex:none}
.what-art{left:366px;top:263px;width:294px;height:505px;background:linear-gradient(180deg,#e4eefa,#f6f9fd);border-radius:4px}
.service-title{left:703px;top:285px;width:400px;font-size:25px;line-height:41px;font-weight:500;color:var(--ink)}
.service-rule{left:690px;top:386px;width:160px;height:1px;background:#bcd9ee}
.service-dot{left:688px;top:383px;width:8px;height:8px;border-radius:50%;background:var(--sky)}
.service-copy{left:703px;top:407px;width:400px;font-size:14px;line-height:29px}
.check-row{left:705px;width:397px;height:50px;background:#fff;border:1px solid var(--line);display:flex;align-items:center;gap:14px;padding:0 16px;font-size:15px;color:var(--ink)}

/* how */
.how{height:793px;background:var(--white)}
.how .title-bar,.benefits .title-bar,.pricing .title-bar{background:var(--purple)}
.step{top:333px;width:290px;text-align:center}
.step-art{width:290px;height:220px;border-radius:14px;background:linear-gradient(180deg,#e6f1fb,#f3f8fd)}
.step h3{margin-top:30px;font-size:21px;font-weight:500;color:var(--ink)}
.step p{margin-top:10px;padding:0 22px;font-size:15px;line-height:29px}

/* benefits */
.benefits{height:737px;background:linear-gradient(135deg,#6a2fe0 0%,var(--purple) 45%,var(--purple-deep) 100%)}
.benefits .section-title{color:#fff;top:90px}
.benefits .title-bar{background:#fff;top:150px}
.benefit{width:470px;display:flex;gap:32px}
.benefit h4{font-size:20px;font-weight:500;color:#fff;letter-spacing:.3px}
.benefit p{margin-top:12px;font-size:15px;line-height:29px;color:#ece6ff}
.btn-white{left:539px;top:608px;width:123px;height:40px;line-height:40px;border-radius:20px;background:#fff;color:var(--purple);font-size:15px}

/* pricing */
.pricing{height:808px;background:var(--cream)}
.plan{background:#fff;text-align:center}
.plan-head{position:relative;background:var(--sky)}
.plan-head h3{color:#fff;font-weight:500;font-size:30px;letter-spacing:1px}
.price{position:absolute;left:50%;transform:translateX(-50%);width:110px;height:110px;border-radius:50%;background:#fff;border:5px solid var(--sky);box-shadow:0 6px 14px rgba(0,0,0,.15);font-family:"Lexend",sans-serif;font-size:32px;font-weight:500;color:var(--sky);line-height:100px}
.plan ul{list-style:none;text-align:left}
.plan li{display:flex;align-items:center;gap:18px;color:var(--ink)}
.plan-foot{border-top:1px dashed #d4d8de;margin:0 6px;font-family:"Lexend",sans-serif;color:var(--purple);font-size:20px}
.plan.pro{box-shadow:0 10px 24px rgba(0,0,0,.08)}
.plan.pro .plan-head{background:var(--purple)}
.plan.pro .price{border-color:var(--purple);color:var(--purple)}

/* footer */
.site-footer{height:429px;background:var(--black);color:#fff}
.foot-col h4{font-size:21px;font-weight:500;margin-bottom:20px}
.foot-col li{list-style:none;display:flex;align-items:center;gap:14px;font-size:15px;line-height:31px}
.contact-item{display:flex;align-items:center;gap:14px;font-size:15px;margin-bottom:28px}
.contact-icon{width:38px;height:38px;border-radius:50%;background:var(--sky);display:flex;align-items:center;justify-content:center;flex:none}
.email-field{border-bottom:1px solid #fff;width:272px;padding-bottom:8px;font-size:15px;margin-top:20px}
.foot-btn{width:137px;height:51px;line-height:51px;font-size:17px;margin-top:32px}
.foot-rule{left:97px;top:362px;width:1005px;height:1px;background:#8a8a8a}
.copyright{left:0;top:392px;width:1200px;text-align:center;font-size:15px}
</style>
</head>
<body>

<header class="site-header">
  <div class="brand abs"><span class="brand-mark"></span>VELTRASHIELD</div>
  <nav class="nav abs"><span class="active">Home</span><span>About Us</span><span>Subscriptions</span><span>Pricing</span></nav>
  <div class="nav-icons abs">
    <svg width="20" height="20" viewBox="0 0 20 20" fill="none" stroke="#1c2233" stroke-width="2"><circle cx="8.5" cy="8.5" r="6"/><path d="M13 13l5 5"/></svg>
    <span style="position:relative">
      <svg width="22" height="20" viewBox="0 0 22 20" fill="none" stroke="#1c2233" stroke-width="2"><path d="M1 2h3l3 11h11l2-8H6"/><circle cx="9" cy="17" r="1.5"/><circle cx="16" cy="17" r="1.5"/></svg>
      <span class="cart-badge">0</span>
    </span>
  </div>
  <a class="btn btn-sky header-cta abs">Contact Us</a>
</header>

<section class="hero">
  <div class="hero-art abs" role="img" aria-label="Glowing digital padlock inside a circuit ring on a dark blue tech background"></div>
  <h1 class="abs">WELCOME TO<br>VELTRASHIELD</h1>
  <p class="abs">Lorem ipsum dolor sit amet, consectetur adipiscing elit, sed do eiusmod tempor incididunt ut labore et dolore magna aliqua.</p>
  <a class="btn btn-sky abs">Subscribe Now</a>
</section>

<section class="what">
  <h2 class="section-title" style="top:90px">WHAT WE DO</h2>
  <div class="title-bar" style="top:142px"></div>
  <p class="lead" style="top:162px">Lorem ipsum dolor sit amet, consectetur adipiscing elit, sed do eiusmod tempor incididunt ut labore et dolore magna aliqua. Ut enim ad minim veniam, quis nostrud exercitation ullamco laboris nisi ut aliquip ex ea commodo consequat.Duis aute irure dolor in reprehenderit in voluptate velit esse cillum dolore eu fugiat nulla pariatur.</p>

  <div class="feature abs" style="top:311px"><svg width="38" height="38" viewBox="0 0 38 38" fill="none" stroke="#3fb0ec" stroke-width="1.6"><path d="M19 5l11 4v9c0 8-5 13-11 15C13 31 8 26 8 18V9z"/></svg><span>Excepteur sint occaecat cupidatat non proident,</span></div>
  <div class="feature abs" style="top:405px"><svg width="38" height="38" viewBox="0 0 38 38" fill="none" stroke="#3fb0ec" stroke-width="1.6"><circle cx="19" cy="19" r="9"/><path d="M19 4v6M19 28v6M4 19h6M28 19h6"/></svg><span>Lorem ipsum dolor sit amet, consectetur</span></div>
  <div class="feature abs" style="top:500px"><svg width="38" height="38" viewBox="0 0 38 38" fill="none" stroke="#3fb0ec" stroke-width="1.6"><path d="M19 5l11 4v9c0 8-5 13-11 15C13 31 8 26 8 18V9z"/><path d="M14 19l4 4 7-8"/></svg><span>Duis aute irure dolor in reprehenderit in</span></div>
  <div class="feature abs" style="top:594px"><svg width="38" height="38" viewBox="0 0 38 38" fill="none" stroke="#3fb0ec" stroke-width="1.6"><rect x="6" y="9" width="26" height="17" rx="2"/><path d="M14 31h10M19 26v5"/></svg><span>Ut enim ad minima veniam, quis nostrum</span></div>

  <div class="what-art abs" role="img" aria-label="Illustration of a laptop with a padlock, shield, folders and circuit lines"></div>

  <h3 class="service-title abs">Cyber Security subscription service</h3>
  <div class="service-rule abs"></div><div class="service-dot abs"></div>
  <p class="service-copy abs">Lorem ipsum dolor sit amet, consectetur adipiscing elit, sed do eiusmod tempor incididunt ut labore et dolore magna aliqua. Duis aute irure dolor in reprehenderit in voluptate velit esse cillum dolore eu fugiat nulla pariatur.</p>
  <div class="check-row abs" style="top:538px"><svg width="22" height="22" viewBox="0 0 22 22" fill="none" stroke="#3fb0ec" stroke-width="1.5"><path d="M11 2l8 3v6c0 5-3 8-8 9-5-1-8-4-8-9V5z"/></svg>Lorem ipsum dolor sit amet, consectetur</div>
  <div class="check-row abs" style="top:603px"><svg width="22" height="22" viewBox="0 0 22 22" fill="none" stroke="#3fb0ec" stroke-width="1.5"><path d="M11 2l8 3v6c0 5-3 8-8 9-5-1-8-4-8-9V5z"/></svg>Lorem ipsum dolor sit amet, consectetur</div>
  <div class="check-row abs" style="top:659px"><svg width="22" height="22" viewBox="0 0 22 22" fill="none" stroke="#3fb0ec" stroke-width="1.5"><path d="M11 2l8 3v6c0 5-3 8-8 9-5-1-8-4-8-9V5z"/></svg>Lorem ipsum dolor sit amet, consectetur</div>
</section>

<section class="how">
  <h2 class="section-title" style="top:80px">WE DIDN'T REINVENT SECURITY, JUST<br>HOW IT'S DELIVERED</h2>
  <div class="title-bar" style="top:177px"></div>
  <p class="lead" style="top:195px">Lorem ipsum dolor sit amet, consectetur adipiscing elit, sed do eiusmod tempor incididunt ut labore et dolore magna aliqua. Ut enim ad minim veniam, quis nostrud exercitation ullamco laboris nisi ut aliquip ex ea commodo consequat. Duis aute irure dolor in reprehenderit in voluptate velit esse cillum dolore eu fugiat nulla pariatur.</p>

  <div class="step abs" style="left:98px"><div class="step-art" role="img" aria-label="Illustration of a phone with a subscribe button and mail envelope"></div><h3>Subscribe</h3><p>Lorem ipsum dolor sit amet, consectetur adipiscing elit, sed do et dolore magna aliqua.</p></div>
  <div class="step abs" style="left:455px"><div class="step-art" role="img" aria-label="Illustration of a large shield and key beside a login window"></div><h3>Request</h3><p>Lorem ipsum dolor sit amet, consectetur adipiscing elit, sed do et dolore magna aliqua.</p></div>
  <div class="step abs" style="left:811px"><div class="step-art" role="img" aria-label="Illustration of a shield with a key next to a password form"></div><h3>Relax</h3><p>Lorem ipsum dolor sit amet, consectetur adipiscing elit, sed do et dolore magna aliqua.</p></div>
</section>

<section class="benefits">
  <h2 class="section-title">SUBSCRIPTION BENEFITS</h2>
  <div class="title-bar"></div>
  <div class="benefit abs" style="left:100px;top:175px"><svg width="54" height="52" viewBox="0 0 54 52" fill="none" stroke="#fff" stroke-width="1.8"><rect x="3" y="10" width="48" height="30" rx="2"/><path d="M20 48h14M27 40v8"/><path d="M27 4l9 4v7c0 6-4 9-9 11-5-2-9-5-9-11V8z"/></svg><div><h4>SED UT PERSPICIATIS UNDE</h4><p>Lorem ipsum dolor sit amet, consectetur adipiscing elit, sed do eiusmod tempor dolore magna aliqua.</p></div></div>
  <div class="benefit abs" style="left:640px;top:175px"><svg width="54" height="52" viewBox="0 0 54 52" fill="none" stroke="#fff" stroke-width="1.8"><rect x="3" y="10" width="48" height="30" rx="2"/><path d="M20 48h14M27 40v8"/><path d="M27 4l9 4v7c0 6-4 9-9 11-5-2-9-5-9-11V8z"/></svg><div><h4>SED UT PERSPICIATIS UNDE</h4><p>Lorem ipsum dolor sit amet, consectetur adipiscing elit, sed do eiusmod tempor dolore magna aliqua.</p></div></div>
  <div class="benefit abs" style="left:100px;top:316px"><svg width="54" height="52" viewBox="0 0 54 52" fill="none" stroke="#fff" stroke-width="1.8"><rect x="3" y="10" width="48" height="30" rx="2"/><path d="M20 48h14M27 40v8"/><path d="M27 4l9 4v7c0 6-4 9-9 11-5-2-9-5-9-11V8z"/></svg><div><h4>SED UT PERSPICIATIS UNDE</h4><p>Lorem ipsum dolor sit amet, consectetur adipiscing elit, sed do eiusmod tempor dolore magna aliqua.</p></div></div>
  <div class="benefit abs" style="left:640px;top:316px"><svg width="54" height="52" viewBox="0 0 54 52" fill="none" stroke="#fff" stroke-width="1.8"><rect x="3" y="10" width="48" height="30" rx="2"/><path d="M20 48h14M27 40v8"/><path d="M27 4l9 4v7c0 6-4 9-9 11-5-2-9-5-9-11V8z"/></svg><div><h4>SED UT PERSPICIATIS UNDE</h4><p>Lorem ipsum dolor sit amet, consectetur adipiscing elit, sed do eiusmod tempor dolore magna aliqua.</p></div></div>
  <div class="benefit abs" style="left:100px;top:457px"><svg width="54" height="52" viewBox="0 0 54 52" fill="none" stroke="#fff" stroke-width="1.8"><rect x="3" y="10" width="48" height="30" rx="2"/><path d="M20 48h14M27 40v8"/><path d="M27 4l9 4v7c0 6-4 9-9 11-5-2-9-5-9-11V8z"/></svg><div><h4>SED UT PERSPICIATIS UNDE</h4><p>Lorem ipsum dolor sit amet, consectetur adipiscing elit, sed do eiusmod tempor dolore magna aliqua.</p></div></div>
  <div class="benefit abs" style="left:640px;top:457px"><svg width="54" height="52" viewBox="0 0 54 52" fill="none" stroke="#fff" stroke-width="1.8"><rect x="3" y="10" width="48" height="30" rx="2"/><path d="M20 48h14M27 40v8"/><path d="M27 4l9 4v7c0 6-4 9-9 11-5-2-9-5-9-11V8z"/></svg><div><h4>SED UT PERSPICIATIS UNDE</h4><p>Lorem ipsum dolor sit amet, consectetur adipiscing elit, sed do eiusmod tempor dolore magna aliqua.</p></div></div>
  <a class="btn btn-white abs">View Nore</a>
</section>

<section class="pricing">
  <h2 class="section-title" style="top:80px">OUR PRICING</h2>
  <div class="title-bar" style="top:135px"></div>

  <div class="plan abs" style="left:103px;top:195px;width:312px;height:470px">
    <div class="plan-head" style="height:138px;padding-top:38px"><h3>FREE</h3><div class="price" style="top:83px">$15</div></div>
    <ul style="padding:80px 0 0 30px;height:258px"><li style="height:40px"><svg width="16" height="14" viewBox="0 0 16 14" fill="none" stroke="#1e8fd0" stroke-width="2.4"><path d="M2 7l4 4 8-9"/></svg>Lorem ipsum dolor sit</li><li style="height:40px"><svg width="16" height="14" viewBox="0 0 16 14" fill="none" stroke="#1e8fd0" stroke-width="2.4"><path d="M2 7l4 4 8-9"/></svg>Duis aute irure dolor</li><li style="height:40px"><svg width="16" height="14" viewBox="0 0 16 14" fill="none" stroke="#1e8fd0" stroke-width="2.4"><path d="M2 7l4 4 8-9"/></svg>Sed ut perspiciatis unde</li><li style="height:40px"><svg width="16" height="14" viewBox="0 0 16 14" fill="none" stroke="#1e8fd0" stroke-width="2.4"><path d="M2 7l4 4 8-9"/></svg>Neque porro quisquam</li></ul>
    <div class="plan-foot" style="height:72px;line-height:66px">View Details &raquo;</div>
  </div>

  <div class="plan pro abs" style="left:415px;top:168px;width:373px;height:524px">
    <div class="plan-head" style="height:165px;padding-top:30px"><h3>PRO</h3><div class="price" style="top:100px">$152</div></div>
    <ul style="padding:85px 0 0 60px;height:277px;font-size:17px"><li style="height:45px"><svg width="16" height="14" viewBox="0 0 16 14" fill="none" stroke="#1e8fd0" stroke-width="2.4"><path d="M2 7l4 4 8-9"/></svg>Lorem ipsum dolor sit</li><li style="height:45px"><svg width="16" height="14" viewBox="0 0 16 14" fill="none" stroke="#1e8fd0" stroke-width="2.4"><path d="M2 7l4 4 8-9"/></svg>Duis aute irure dolor</li><li style="height:45px"><svg width="16" height="14" viewBox="0 0 16 14" fill="none" stroke="#1e8fd0" stroke-width="2.4"><path d="M2 7l4 4 8-9"/></svg>Sed ut perspiciatis unde</li><li style="height:45px"><svg width="16" height="14" viewBox="0 0 16 14" fill="none" stroke="#1e8fd0" stroke-width="2.4"><path d="M2 7l4 4 8-9"/></svg>Neque porro quisquam</li></ul>
    <div class="plan-foot" style="height:82px;line-height:76px;margin:0 28px">View Details &raquo;</div>
  </div>

  <div class="plan abs" style="left:788px;top:195px;width:313px;height:470px">
    <div class="plan-head" style="height:138px;padding-top:38px"><h3>ADVANCED</h3><div class="price" style="top:83px">$12</div></div>
    <ul style="padding:80px 0 0 30px;height:258px"><li style="height:40px"><svg width="16" height="14" viewBox="0 0 16 14" fill="none" stroke="#1e8fd0" stroke-width="2.4"><path d="M2 7l4 4 8-9"/></svg>Lorem ipsum dolor sit</li><li style="height:40px"><svg width="16" height="14" viewBox="0 0 16 14" fill="none" stroke="#1e8fd0" stroke-width="2.4"><path d="M2 7l4 4 8-9"/></svg>Duis aute irure dolor</li><li style="height:40px"><svg width="16" height="14" viewBox="0 0 16 14" fill="none" stroke="#1e8fd0" stroke-width="2.4"><path d="M2 7l4 4 8-9"/></svg>Sed ut perspiciatis unde</li><li style="height:40px"><svg width="16" height="14" viewBox="0 0 16 14" fill="none" stroke="#1e8fd0" stroke-width="2.4"><path d="M2 7l4 4 8-9"/></svg>Neque porro quisquam</li></ul>
    <div class="plan-foot" style="height:72px;line-height:66px">View Details &raquo;</div>
  </div>
</section>

<footer class="site-footer">
  <div class="foot-col abs" style="left:97px;top:62px"><h4>Quick Links</h4><ul>
    <li><svg width="14" height="12" viewBox="0 0 14 12" fill="none" stroke="#fff" stroke-width="2.4"><path d="M1 6h11M7 1l5 5-5 5"/></svg>Home</li>
    <li><svg width="14" height="12" viewBox="0 0 14 12" fill="none" stroke="#fff" stroke-width="2.4"><path d="M1 6h11M7 1l5 5-5 5"/></svg>About Us</li>
    <li><svg width="14" height="12" viewBox="0 0 14 12" fill="none" stroke="#fff" stroke-width="2.4"><path d="M1 6h11M7 1l5 5-5 5"/></svg>Subscriptions</li>
    <li><svg width="14" height="12" viewBox="0 0 14 12" fill="none" stroke="#fff" stroke-width="2.4"><path d="M1 6h11M7 1l5 5-5 5"/></svg>Pricing</li>
    <li><svg width="14" height="12" viewBox="0 0 14 12" fill="none" stroke="#fff" stroke-width="2.4"><path d="M1 6h11M7 1l5 5-5 5"/></svg>Contact Us</li></ul></div>
  <div class="foot-col abs" style="left:296px;top:62px"><h4>Other Links</h4><ul>
    <li><svg width="14" height="12" viewBox="0 0 14 12" fill="none" stroke="#fff" stroke-width="2.4"><path d="M1 6h11M7 1l5 5-5 5"/></svg>FAQ</li>
    <li><svg width="14" height="12" viewBox="0 0 14 12" fill="none" stroke="#fff" stroke-width="2.4"><path d="M1 6h11M7 1l5 5-5 5"/></svg>Tems of Use</li>
    <li><svg width="14" height="12" viewBox="0 0 14 12" fill="none" stroke="#fff" stroke-width="2.4"><path d="M1 6h11M7 1l5 5-5 5"/></svg>Privacy Policy</li>
    <li><svg width="14" height="12" viewBox="0 0 14 12" fill="none" stroke="#fff" stroke-width="2.4"><path d="M1 6h11M7 1l5 5-5 5"/></svg>Support Links</li>
    <li><svg width="14" height="12" viewBox="0 0 14 12" fill="none" stroke="#fff" stroke-width="2.4"><path d="M1 6h11M7 1l5 5-5 5"/></svg>Conditions</li></ul></div>
  <div class="foot-col abs" style="left:507px;top:62px"><h4>Contact Us</h4>
    <div class="contact-item"><span class="contact-icon"><svg width="16" height="18" viewBox="0 0 16 18" fill="#fff"><path d="M8 0a6 6 0 0 0-6 6c0 5 6 12 6 12s6-7 6-12a6 6 0 0 0-6-6zm0 8.5A2.5 2.5 0 1 1 8 3.5a2.5 2.5 0 0 1 0 5z"/></svg></span>Company Name,United State.</div>
    <div class="contact-item"><span class="contact-icon"><svg width="18" height="14" viewBox="0 0 18 14" fill="none" stroke="#fff" stroke-width="1.8"><rect x="1" y="1" width="16" height="12" rx="1"/><path d="M1 2l8 6 8-6"/></svg></span>info@veltrashield.example</div>
    <div class="contact-item"><span class="contact-icon"><svg width="16" height="16" viewBox="0 0 16 16" fill="#fff"><path d="M3.5 1l2.5 3-1.5 2a9 9 0 0 0 5 5l2-1.5 3 2.5-1.5 3C7 15 1 9 1 2.5z"/></svg></span>+1 555 0100 2000</div>
  </div>
  <div class="foot-col abs" style="left:828px;top:62px;width:280px"><h4>Sign Up Our To Newsletter</h4>
    <p style="font-size:14px;line-height:29px">Lorem ipsum dolor sit amet,consectetur adipiscing elit,adipiscing elit.</p>
    <div class="email-field">Email</div>
    <a class="btn btn-sky foot-btn" style="margin-left:8px">Subscribe</a>
  </div>
  <div class="foot-rule abs"></div>
  <p class="copyright abs">Copyrights@2024.Veltrashield.All Rights Reserved</p>
</footer>

</body>
</html>
```